Business card needed for home based pen making business.

I'm after a business card that's a bit more than an off the shelf card. I do like the idea of a card split horizontal with different colours used. A third colour is to be used for the business name and if need a forth for the other details.

I don't have a logo and will pay extra for one ($150 extra). I mainly make pens and seam rippers (stitch unpicks). The logo may be used for a website in future, as will the colours so please provide the colour codes and font type.

I'd like the business name in an easy to read script font at the top (with logo if you have one) and the other details to the bottom left hand side. I'll leave it up to you to match the script to the font used for the other details.

I'd like to keep a triangular balance to the card so something like a siloet of pot containing pens on the bottom right could be used to balance it out. There my ideas I want to see your.

Business name: Quillo & Co
Email address: quilloandco@mailvista.net
Contact: Dorian
Phone: 0418 352 976
No address is to be used on card.

Target Market(s)

Wide variety of people visiting craft markets. Age range 30+.

Industry/Entity Type

Business

Contact Information for Business Card

Quill & Co

Font styles to use
Script

Colors
f0ecf4
3277b5
3176b5

Requirements
Must have
• Contact: Dorian
• Phone: 0418 352 976
• Email address: quilloandco@mailvista.net
Nice to have
• An icon and/or graphics depicting pens and seam rippers..
Should not have
• I don't want icon/ graphic to be a crossed pen and seam ripper.

```html
<!DOCTYPE html>
<html lang="en">
<head>
<meta charset="utf-8">
<title>Quillo &amp; Co — Business Card</title>
<link rel="stylesheet" href="https://fonts.googleapis.com/css2?family=Courgette&family=Open+Sans:wght@400;600&display=swap">
<style>
  :root {
    --backdrop-top: #3f6fb8;
    --backdrop-bottom: #1c2f5c;
    --card-blue: #3277b5;
    --card-blue-deep: #2a5f9c;
    --card-blue-bright: #2f7fd0;
    --card-slate: #4e6478;
    --card-slate-dark: #44586b;
    --divider: #c9d3de;
    --ink-light: #f0ecf4;
  }
  html, body {
    margin: 0;
    padding: 0;
    width: 1200px;
    height: 900px;
    overflow: hidden;
  }
  body {
    background: linear-gradient(160deg, var(--backdrop-top) 0%, var(--backdrop-bottom) 100%);
    display: flex;
    align-items: center;
    justify-content: center;
  }
  .business-card {
    position: relative;
    width: 900px;
    height: 540px;
    border-radius: 6px;
    overflow: hidden;
    box-shadow: 0 24px 60px rgba(5, 15, 40, 0.55);
  }
  .card-facets {
    position: absolute;
    inset: 0;
    width: 100%;
    height: 100%;
  }
  .brand-block {
    position: absolute;
    top: 58px;
    right: 150px;
    text-align: right;
  }
  .brand-name {
    margin: 0;
    font-family: "Courgette", cursive;
    font-weight: 400;
    font-size: 64px;
    line-height: 1;
    color: var(--ink-light);
    letter-spacing: 1px;
  }
  .contact-person {
    margin: 10px 0 0;
    font-family: "Open Sans", sans-serif;
    font-size: 26px;
    color: var(--ink-light);
  }
  .contact-details {
    position: absolute;
    left: 170px;
    bottom: 70px;
    list-style: none;
    margin: 0;
    padding: 0;
  }
  .contact-details li {
    display: flex;
    align-items: center;
    gap: 22px;
    font-family: "Courgette", cursive;
    color: var(--ink-light);
  }
  .contact-phone { font-size: 42px; margin-bottom: 14px; }
  .contact-email { font-size: 34px; }
  .contact-icon { flex: none; }
</style>
</head>
<body>
  <article class="business-card">
    <svg class="card-facets" viewBox="0 0 900 540" preserveAspectRatio="none" aria-hidden="true">
      <rect width="900" height="540" fill="var(--card-blue)"/>
      <polygon points="0,0 900,0 900,540" fill="var(--card-blue-deep)" opacity="0.35"/>
      <polygon points="0,0 900,540 0,540" fill="var(--card-slate)"/>
      <polygon points="0,0 330,540 0,540" fill="var(--card-blue-bright)"/>
      <polygon points="0,0 330,540 520,540" fill="var(--card-slate-dark)" opacity="0.35"/>
      <line x1="0" y1="0" x2="900" y2="540" stroke="var(--divider)" stroke-width="4"/>
    </svg>

    <header class="brand-block">
      <h1 class="brand-name">Quillo &amp; Co</h1>
      <p class="contact-person">Dorian</p>
    </header>

    <ul class="contact-details">
      <li class="contact-phone">
        <svg class="contact-icon" width="26" height="38" viewBox="0 0 26 38" aria-hidden="true">
          <rect x="2" y="2" width="22" height="34" rx="3" fill="none" stroke="var(--ink-light)" stroke-width="3"/>
          <line x1="9" y1="31" x2="17" y2="31" stroke="var(--ink-light)" stroke-width="2"/>
        </svg>
        0418 352 976
      </li>
      <li class="contact-email">
        <svg class="contact-icon" width="30" height="30" viewBox="0 0 30 30" aria-hidden="true">
          <circle cx="15" cy="15" r="13" fill="var(--ink-light)"/>
          <circle cx="15" cy="15" r="7" fill="none" stroke="var(--card-slate)" stroke-width="2"/>
          <line x1="8" y1="15" x2="22" y2="15" stroke="var(--card-slate)" stroke-width="2"/>
        </svg>
        quilloandco@mailvista.net
      </li>
    </ul>
  </article>
</body>
</html>
```